Water Filter Company Needs Bizz Cards!!

Need business cards for my company. We sell whole home water filters and salt free water softeners. No more buying bottled water. Our filtering units filter out all heavy metals, chlorine, and VOC's, last 15 years, and are maintenance free and supply your whole home with spring quality alkaline water. Our Salt free water conditioners, eliminate hard water and scale, without lowering the ph, or TDS's (total Dissolved solids)

I think this is the color code we are using on my site. My logo looks good behind it. #192841

Website will be www.Brovexa.com

Industry/Entity Type

Water Purification

Contact Information for Business Card

For now, just insert standard Dummy text. I need these text lines for the info to be editable so i can make them for multiple employees. I do have Photoshop and illustrator, unless there is a simpler program i can use solely for biz cards

Font styles to use
Sans Serif

Requirements
Must have
• Use my preexisting logo.

www.BroVexa.com

Spring Quality Alkaline Water at every tap.

List out services. Whole Home Water Filters, Salt Free Water Softeners, Clarimont KT7, UV Sterilizers
Nice to have
• I think this is the color code we are using on my site. My logo looks good behind it. #192841 or black. Please no white or light blue backgrounds.

Maybe a picture of my tank.

Slogan like Spring Quality Alkaline Water at every tap.
And just list the services Whole Home Water Filters, Salt Free Water Softeners, Clarimont KT7, UV Sterilizers

I think I would like to not have a contrasting textured logo like I see on some of them. I may use it for my personal cards, but new employees may not want the extra expense.
Should not have
• A different logo than the one provided.

White or baby blue backgrounds. Use the color code, or blacks.

```html
<!DOCTYPE html>
<html lang="en">
<head>
<meta charset="utf-8">
<title>Brovexa Water Systems – Business Cards</title>
<link href="https://fonts.googleapis.com/css2?family=Roboto:wght@300;400;500;700&display=swap" rel="stylesheet">
<style>
  :root {
    --backdrop: #e6e8eb;
    --ink-black: #0a0a0a;
    --brand-blue: #0b8fd4;
    --sky-blue: #38bdee;
    --band-grey: #b6b9bd;
    --ring-grey: #c9ccd0;
    --text-grey: #9a9da1;
    --paper: #ffffff;
  }
  * { box-sizing: border-box; margin: 0; padding: 0; }
  html, body {
    width: 1200px; height: 1124px; overflow: hidden;
    background: var(--backdrop);
    font-family: "Roboto", Arial, sans-serif;
  }
  .canvas { position: relative; width: 1200px; height: 1124px; }
  .card {
    position: absolute; left: 150px; width: 900px; height: 514px;
    overflow: hidden; box-shadow: 0 6px 18px rgba(0,0,0,.18);
  }

  /* Back of card */
  .card-back { top: 32px; background: var(--brand-blue); }
  .back-top {
    position: absolute; left: 0; top: 0; width: 100%; height: 180px;
    background: var(--ink-black);
    display: flex; justify-content: center; align-items: center; padding-bottom: 30px;
  }
  .wordmark { display: flex; align-items: center; gap: 14px; }
  .wordmark-dot { width: 34px; height: 34px; border-radius: 50%; background: var(--sky-blue); }
  .wordmark-name { font-weight: 700; font-size: 62px; letter-spacing: -1px; color: var(--sky-blue); line-height: 1; }
  .product-row {
    position: absolute; left: 0; top: 140px; width: 100%;
    display: flex; justify-content: center; gap: 110px;
  }
  .product-ring {
    width: 176px; height: 176px; border-radius: 50%;
    background: var(--ring-grey); padding: 8px;
  }
  .product-ring .photo {
    width: 100%; height: 100%; border-radius: 50%; border: 6px solid var(--paper);
    background: radial-gradient(circle, #f4f5f6 0%, #dfe2e5 100%);
  }
  .slogan-band {
    position: absolute; left: 0; top: 382px; width: 100%; height: 58px;
    background: var(--band-grey); color: var(--paper);
    font-size: 27px; font-weight: 400; letter-spacing: 1px; text-transform: uppercase;
    display: flex; align-items: center; justify-content: center;
  }
  .services-band {
    position: absolute; left: 0; top: 440px; width: 100%; height: 74px;
    background: var(--sky-blue); color: var(--paper);
    font-size: 22px; font-weight: 500;
    display: flex; align-items: center; justify-content: center; gap: 12px;
  }

  /* Front of card */
  .card-front { top: 578px; background: var(--paper); }
  .front-logo { position: absolute; left: 60px; top: 50px; }
  .front-logo .wordmark-dot { width: 26px; height: 26px; }
  .front-logo .wordmark-name { font-size: 50px; color: var(--sky-blue); }
  .person { position: absolute; left: 60px; top: 142px; }
  .person-name { font-size: 34px; font-weight: 500; color: var(--sky-blue); }
  .person-title { font-size: 21px; font-weight: 300; color: var(--text-grey); margin-top: 2px; }
  .address {
    position: absolute; left: 60px; top: 242px;
    font-size: 23px; font-weight: 300; color: var(--text-grey); line-height: 1.25;
  }
  .contact-list { position: absolute; left: 60px; top: 336px; list-style: none; }
  .contact-list li {
    display: flex; align-items: center; gap: 16px;
    font-size: 23px; font-weight: 300; color: var(--text-grey); height: 38px;
  }
  .contact-list svg { width: 20px; height: 20px; flex: none; }
  .contact-list .web { color: var(--sky-blue); }
  .front-accent {
    position: absolute; right: -60px; bottom: -120px; width: 380px; height: 380px;
    border-radius: 50%; background: var(--sky-blue); opacity: .18;
  }
</style>
</head>
<body>
<main class="canvas">

  <section class="card card-back" aria-label="Business card back">
    <div class="back-top">
      <div class="wordmark">
        <span class="wordmark-dot"></span>
        <span class="wordmark-name">Brovexa</span>
      </div>
    </div>
    <div class="product-row">
      <div class="product-ring"><div class="photo" role="img" aria-label="Photo of a black whole home water filter"></div></div>
      <div class="product-ring"><div class="photo" role="img" aria-label="Photo of a salt free water softener tank"></div></div>
      <div class="product-ring"><div class="photo" role="img" aria-label="Photo of a UV sterilizer unit"></div></div>
    </div>
    <div class="slogan-band">Spring quality alkaline water at every tap</div>
    <div class="services-band">
      <span>whole home water filters</span><span>•</span>
      <span>salt free water softeners</span><span>•</span>
      <span>Clarimont KT7</span><span>•</span>
      <span>UV Sterilizers</span>
    </div>
  </section>

  <section class="card card-front" aria-label="Business card front">
    <div class="front-logo wordmark">
      <span class="wordmark-dot"></span>
      <span class="wordmark-name">Brovexa</span>
    </div>
    <div class="person">
      <p class="person-name">Daniel Harper</p>
      <p class="person-title">Manager</p>
    </div>
    <address class="address" style="font-style:normal">
      4820 Harbor Lane<br>Portland OR, USA
    </address>
    <ul class="contact-list">
      <li>
        <svg viewBox="0 0 24 24" aria-hidden="true"><path fill="#38bdee" d="M6.6 10.8a15.1 15.1 0 0 0 6.6 6.6l2.2-2.2a1 1 0 0 1 1-.25 11.4 11.4 0 0 0 3.6.57 1 1 0 0 1 1 1V20a1 1 0 0 1-1 1A17 17 0 0 1 3 4a1 1 0 0 1 1-1h3.5a1 1 0 0 1 1 1c0 1.25.2 2.45.57 3.57a1 1 0 0 1-.25 1z"/></svg>
        ( 84) 0987 654 321
      </li>
      <li>
        <svg viewBox="0 0 24 24" aria-hidden="true"><rect x="2.5" y="5" width="19" height="14" rx="1.5" fill="none" stroke="#38bdee" stroke-width="2"/><path d="M3 6l9 7 9-7" fill="none" stroke="#38bdee" stroke-width="2"/></svg>
        contact@brovexa.com
      </li>
      <li>
        <svg viewBox="0 0 24 24" aria-hidden="true"><circle cx="12" cy="12" r="9.5" fill="none" stroke="#38bdee" stroke-width="2"/><ellipse cx="12" cy="12" rx="4" ry="9.5" fill="none" stroke="#38bdee" stroke-width="1.6"/><path d="M2.5 12h19M4 7h16M4 17h16" stroke="#38bdee" stroke-width="1.6"/></svg>
        <span class="web">www.Brovexa.com</span>
      </li>
    </ul>
    <div class="front-accent" aria-hidden="true"></div>
  </section>

</main>
</body>
</html>
```